Business card for an e-commerce/social networking website
Bazorin
Simple
Yousef Karim AlShehhi
Chief Financial Officer
Palm Crest Isle, Orchid Court Apt 418 Abu Dhabi, United Arab Emirates
1-800-BAZORIN
alshehhi@bazorin.ae
www.Bazorin.ae
the card be contemporary. easy on the eye. not cluttered.
the single "B" in the box.

```html
<!DOCTYPE html>
<html lang="en">
<head>
<meta charset="utf-8">
<title>Bazorin Business Card</title>
<link href="https://fonts.googleapis.com/css2?family=Open+Sans:wght@400;600;700&display=swap" rel="stylesheet">
<style>
  :root{
    --bg:#e9ebee;
    --card:#ffffff;
    --blue:#2a7fc4;
    --blue-deep:#1565a8;
    --blue-light:#8cc3ea;
    --blue-pale:#e3f0fa;
    --ink:#5a5f66;
    --ink-soft:#8a9098;
  }
  *{margin:0;padding:0;box-sizing:border-box}
  html,body{width:1200px;height:1009px;overflow:hidden;background:var(--bg);
    font-family:"Open Sans",Arial,sans-serif;color:var(--ink)}
  .card{position:absolute;left:190px;width:820px;height:468px;background:var(--card);
    border-radius:22px;box-shadow:0 6px 18px rgba(0,0,0,.12);overflow:hidden}
  .card--front{top:42px}
  .card--back{top:540px}

  .logo-box{position:absolute;left:50%;top:50px;transform:translateX(-50%);
    width:120px;height:100px;border-radius:14px;background:var(--card);
    box-shadow:0 3px 10px rgba(0,0,0,.16);display:flex;align-items:center;justify-content:center}
  .logo-box .initial{font-size:64px;font-weight:700;line-height:1;color:var(--blue)}

  .person{position:absolute;left:0;right:0;top:172px;text-align:center}
  .person .name{font-size:22px;font-weight:700;color:var(--blue-deep)}
  .person .role{font-size:15px;color:var(--ink-soft);margin-top:2px}

  .address{position:absolute;left:56px;top:252px;font-size:14px;line-height:1.55;color:var(--ink)}
  .contacts{position:absolute;right:60px;top:230px;list-style:none;font-size:14px;line-height:1.7;color:var(--ink)}
  .contacts li{display:flex;align-items:center;gap:10px}
  .contacts svg{width:14px;height:14px;flex:none}

  .accent-band{position:absolute;left:0;right:0;bottom:0;height:80px;
    background:linear-gradient(180deg,var(--blue-light) 0%,var(--blue) 55%,var(--blue-deep) 100%)}

  .back-url{position:absolute;left:34px;top:50%;transform:translate(-50%,-50%) rotate(-90deg);
    transform-origin:center;font-size:15px;font-weight:600;letter-spacing:9px;color:var(--blue);
    white-space:nowrap;margin-left:10px}
  .back-mark{position:absolute;right:110px;top:74px;width:320px;height:320px;border-radius:50%;
    background:var(--blue-pale)}
</style>
</head>
<body>
  <section class="card card--front">
    <div class="logo-box"><span class="initial">B</span></div>

    <div class="person">
      <p class="name">Yousef Karim AlShehhi</p>
      <p class="role">Chief Financial Officer</p>
    </div>

    <p class="address">Palm Crest Isle, Orchid Court Apt 418<br>Abu Dhabi, United Arab Emirates</p>

    <ul class="contacts">
      <li><svg viewBox="0 0 14 14"><circle cx="7" cy="7" r="7" fill="var(--blue)"/><path d="M4.5 3.5l1.6 0 .6 1.8-1 .8a5 5 0 0 0 2.2 2.2l.8-1 1.8.6 0 1.6c-3.6.3-6.3-2.4-6-6z" fill="#fff"/></svg>1-800-BAZORIN</li>
      <li><svg viewBox="0 0 14 14"><circle cx="7" cy="7" r="7" fill="var(--blue)"/><rect x="5" y="3" width="4" height="8" rx="1" fill="#fff"/></svg>+971 50 417 362 9</li>
      <li><svg viewBox="0 0 14 14"><circle cx="7" cy="7" r="7" fill="var(--blue)"/><path d="M4.5 3.5l1.6 0 .6 1.8-1 .8a5 5 0 0 0 2.2 2.2l.8-1 1.8.6 0 1.6c-3.6.3-6.3-2.4-6-6z" fill="#fff"/></svg>02 640 3318</li>
      <li><svg viewBox="0 0 14 14"><circle cx="7" cy="7" r="7" fill="var(--blue)"/><rect x="3.5" y="4" width="7" height="6" fill="#fff"/></svg>02 640 3319</li>
      <li><svg viewBox="0 0 14 14"><circle cx="7" cy="7" r="7" fill="var(--blue)"/><rect x="3.5" y="4.5" width="7" height="5" fill="#fff"/><path d="M3.5 4.5l3.5 3 3.5-3" stroke="var(--blue)" fill="none" stroke-width=".8"/></svg>alshehhi@bazorin.ae</li>
      <li><svg viewBox="0 0 14 14"><circle cx="7" cy="7" r="7" fill="var(--blue)"/><circle cx="7" cy="7" r="3.5" fill="none" stroke="#fff" stroke-width="1"/><path d="M3.5 7h7M7 3.5v7" stroke="#fff" stroke-width=".8"/></svg>www.Bazorin.ae</li>
    </ul>

    <div class="accent-band" role="img" aria-label="Decorative blue wave band along the bottom edge"></div>
  </section>

  <section class="card card--back">
    <p class="back-url">www.Bazorin.ae</p>
    <div class="back-mark"></div>
  </section>
</body>
</html>
```